I need a two page flyer (one page front and back) outlining our residential furniture rental options.

Title: Premium Residential Furniture Rentals

GOOD
Our Brimwell Orla Furniture Package is designed to offer a perfect balance of affordability and style, without compromising on quality. This package features a selection of functional and aesthetically pleasing furniture pieces, ideal for those looking to create a polished and professional space. With quick installation handled by our experienced in-house team, you can expect a smooth and hassle-free setup. This package ensures both convenience and value, providing a streamlined solution for your needs.
Living room, dining room and bedroom (additional bedrooms available)
- $710/month with a 3 month commitment
- $570/month with a 6 month commitment

BETTER
Our Premium Furniture Package takes comfort and style to the next level, offering an enhanced experience compared to our Orla option. Carefully selected with durability in mind, this package features high-quality, convenient furniture designed for both functionality and aesthetics. Perfect for those seeking a more refined look and superior comfort, it’s ideal for creating a sophisticated and inviting environment. With attention to detail in both design and craftsmanship, the premium package elevates any space, ensuring a higher standard of comfort and style that caters to both employees and clients.
- $1,150/month with a 3 month commitment
- $900/month with a 6 month commitment

BEST
Our Custom Furniture Package offers a tailored experience where you’ll work directly with our expert designer to create the ultimate luxurious and functional space. We include lounging, dining, sleeping and working from home, this package allows you to curate a space that perfectly fits your needs and style. With personalized attention to detail, we ensure every element is designed to provide the highest level of comfort, convenience, and elegance, transforming your space into a sophisticated sanctuary for relaxation and enjoyment.
Please inquire for pricing

www.quilbyhomeleasing.com

```html
<!DOCTYPE html>
<html lang="en">
<head>
<meta charset="utf-8">
<title>Premium Residential Furniture Rentals – Quilby Home Leasing</title>
<link rel="stylesheet" href="https://fonts.googleapis.com/css2?family=Open+Sans:ital,wght@0,400;0,600;0,800;1,400;1,600;1,800&family=Montserrat:wght@400&display=swap">
<style>
  :root {
    --backdrop: #a9a9a9;
    --paper: #ffffff;
    --mauve: #bcb0b8;
    --mauve-ink: #b4a4b0;
    --sand: #d8cfc4;
    --ink: #0b0b0b;
    --text: #1c1c1c;
    --cream: #f1ece4;
    --photo-a: #e6e3e0;
    --photo-b: #4c4a4c;
  }
  * { margin: 0; padding: 0; box-sizing: border-box; }
  html, body { width: 1200px; height: 2226px; overflow: hidden; }
  body { background: var(--backdrop); font-family: "Open Sans", Arial, sans-serif; color: var(--text); position: relative; }

  .page { position: absolute; left: 236px; width: 729px; height: 1030px; background: var(--paper); overflow: hidden; }
  .page--front { top: 58px; }
  .page--back { top: 1138px; }
  .page > * { position: absolute; }

  .brand { display: flex; align-items: center; gap: 10px; font-family: "Montserrat", Arial, sans-serif; font-weight: 400; color: var(--ink); white-space: nowrap; }
  .brand__mark { width: 14px; height: 14px; background: var(--ink); }
  .brand--large { left: 395px; top: 160px; font-size: 19px; }
  .brand--small { left: 520px; top: 102px; font-size: 14px; }
  .brand--small .brand__mark { width: 11px; height: 11px; }

  .photo { border: 0; }
  .photo--living { left: 18px; top: 291px; width: 711px; height: 364px; background: linear-gradient(100deg, var(--photo-b) 0%, #8a8584 30%, var(--photo-a) 55%, #6b6667 80%, #3f3d3f 100%); }
  .photo--kitchen { left: 0; top: 100px; width: 516px; height: 343px; background: linear-gradient(160deg, #eef0f2 0%, #c9b9a3 45%, #d9d5cf 70%, #f3f2f0 100%); }

  .title-panel { left: 49px; top: 100px; width: 369px; height: 367px; background: var(--mauve); padding: 64px 0 0 32px; }
  .title-panel h1 { font-weight: 800; font-size: 49px; line-height: 58.5px; color: #fff; letter-spacing: 0.3px; }

  .tier-frame { border: 3px solid var(--sand); }
  .tier-label { background: var(--ink); color: var(--cream); font-style: italic; font-weight: 800; font-size: 33px; display: flex; align-items: center; justify-content: center; letter-spacing: 0.5px; }

  .good-frame { left: 44px; top: 621px; width: 270px; height: 83px; }
  .good-label { left: 64px; top: 631px; width: 256px; height: 63px; }

  .copy { font-size: 12.4px; line-height: 14.7px; text-align: justify; }
  .copy em { font-style: italic; font-weight: 600; }
  .copy .rooms { display: block; text-align: left; }

  .good-copy { left: 49px; top: 755px; width: 631px; }

  .prices { list-style: none; }
  .prices li { display: flex; align-items: baseline; gap: 6px; font-size: 14.5px; height: 27px; }
  .prices .amount { font-style: italic; font-weight: 800; font-size: 20px; color: var(--mauve-ink); }
  .good-prices { left: 49px; top: 862px; }

  .accent-frame { border: 3px solid var(--sand); }
  .accent-block { background: var(--ink); }
  .accent-band { background: var(--mauve); }

  .front-frame { left: 519px; top: 933px; width: 122px; height: 120px; }
  .front-block-a { left: 579px; top: 948px; width: 58px; height: 45px; }
  .front-block-b { left: 641px; top: 948px; width: 60px; height: 82px; }
  .front-band { left: 418px; top: 993px; width: 258px; height: 37px; }

  .better-frame { left: 226px; top: 188px; width: 270px; height: 83px; }
  .better-label { left: 245px; top: 199px; width: 256px; height: 63px; z-index: 2; }
  .better-panel { left: 278px; top: 230px; width: 451px; height: 425px; background: var(--mauve); }
  .better-copy { left: 320px; top: 333px; width: 360px; color: var(--ink); }
  .better-prices { left: 320px; top: 525px; }
  .better-prices .amount { color: #fff; }

  .best-frame { left: 0; top: 608px; width: 116px; height: 83px; }
  .best-label { left: 0; top: 618px; width: 254px; height: 63px; }
  .best-copy { left: 49px; top: 730px; width: 631px; }
  .best-prices { left: 49px; top: 818px; }
  .best-prices li { font-size: 12px; }

  .back-frame { left: 426px; top: 883px; width: 122px; height: 100px; }
  .back-block { left: 486px; top: 900px; width: 119px; height: 130px; }
  .back-block::after { content: ""; position: absolute; left: 58px; top: 0; width: 4px; height: 100%; background: var(--paper); }
  .web-band { left: 156px; top: 944px; width: 426px; height: 64px; display: flex; align-items: center; justify-content: center; color: #fff; font-size: 16px; font-weight: 600; letter-spacing: 2.2px; }
</style>
</head>
<body>

<section class="page page--front">
  <div class="photo photo--living" role="img" aria-label="Photo of a furnished living room with a white sofa, gold coffee table, framed wall art and flowers"></div>
  <div class="title-panel"><h1>PREMIUM<br>RESIDENTIAL<br>FURNITURE<br>RENTALS</h1></div>
  <div class="brand brand--large"><span class="brand__mark"></span>QUILBY HOME LEASING</div>

  <div class="tier-frame good-frame"></div>
  <div class="tier-label good-label">GOOD</div>

  <p class="copy good-copy"><em>Our Brimwell Orla Furniture Package is designed to offer a perfect balance of affordability and style, without compromising on quality.</em> This package features a selection of functional and aesthetically pleasing furniture pieces, ideal for those looking to create a polished and professional space. With quick installation handled by our experienced in-house team, you can expect a smooth and hassle-free setup. This package ensures both convenience and value, providing a streamlined solution for your needs.<span class="rooms">Living room, dining room and bedroom (additional bedrooms available)</span></p>

  <ul class="prices good-prices">
    <li><span class="amount">- $710/month</span> with a 3 month commitment</li>
    <li><span class="amount">- $570/month</span> with a 6 month commitment</li>
  </ul>

  <div class="accent-frame front-frame"></div>
  <div class="accent-block front-block-a"></div>
  <div class="accent-block front-block-b"></div>
  <div class="accent-band front-band"></div>
</section>

<section class="page page--back">
  <div class="brand brand--small"><span class="brand__mark"></span>QUILBY HOME LEASING</div>
  <div class="photo photo--kitchen" role="img" aria-label="Photo of an open-plan apartment with kitchen bar stools, a round wooden coffee table and a sofa"></div>

  <div class="better-panel"></div>
  <div class="tier-frame better-frame"></div>
  <div class="tier-label better-label">BETTER</div>

  <p class="copy better-copy"><em>Our Premium Furniture Package takes comfort and style to the next level, offering an enhanced experience compared to our Orla option.</em> Carefully selected with durability in mind, this package features high-quality, convenient furniture designed for both functionality and aesthetics. Perfect for those seeking a more refined look and superior comfort, it’s ideal for creating a sophisticated and inviting environment. With attention to detail in both design and craftsmanship, the premium package elevates any space, ensuring a higher standard of comfort and style that caters to both employees and clients.<span class="rooms">Living room, dining room and bedroom (additional bedrooms available)</span></p>

  <ul class="prices better-prices">
    <li><span class="amount">- $1,150/month</span> with a 3 month commitment</li>
    <li><span class="amount">- $900/month</span> with a 6 month commitment</li>
  </ul>

  <div class="tier-frame best-frame"></div>
  <div class="tier-label best-label">BEST</div>

  <p class="copy best-copy"><em>Our Custom Furniture Package offers a tailored experience where you’ll work directly with our expert designer to create the ultimate luxurious and functional space.</em> We include lounging, dining, sleeping and working from home, this package allows you to curate a space that perfectly fits your needs and style. With personalized attention to detail, we ensure every element is designed to provide the highest level of comfort, convenience, and elegance, transforming your space into a sophisticated sanctuary for relaxation and enjoyment.</p>

  <ul class="prices best-prices">
    <li><span class="amount">- $1,150/month</span> with a 3 month commitment</li>
    <li><span class="amount">- $900/month</span> with a 6 month commitment</li>
  </ul>

  <div class="accent-frame back-frame"></div>
  <div class="accent-block back-block"></div>
  <div class="accent-band web-band">www.quilbyhomeleasing.com</div>
</section>

</body>
</html>
```